Curbside Bin Butler Valet Trash Recycling

I want to create a colorful brochure, I really like my company colors, with basic information about valet trash for apartment complexes. You can include some apartment recycling information as well, but 80% trash, 20% recycling. I have included my logo in the attachments. Also, you can find information at curbsidebinbutler.example, very basic and I will be redoing my website as well.

many people are giving information about business and residential recycling, I only want information on trash and recycling valet for apartments

Target Market(s)

apartment complex tenants and management

Industry/Entity Type

Apartment

Number of Pages Required

4 page

Font styles to use
Serif
Sans Serif

Colors
9bcb3b
f37122
0355a3

Requirements
Must have
• Tri-Fold brochure, colorful, well organized. Advantages for tenants and for property management.

```html
<!DOCTYPE html>
<html lang="en">
<head>
<meta charset="utf-8">
<title>Curbside Bin Butler – Valet Trash Tri-Fold Brochure</title>
<link href="https://fonts.googleapis.com/css2?family=Signika:wght@400;600;700&family=Questrial&display=swap" rel="stylesheet">
<style>
:root{
  --green:#9bcb3b;
  --green-deep:#5fae32;
  --orange:#f37122;
  --blue:#0355a3;
  --sky:#1e9ad6;
  --charcoal:#3a3b3c;
  --paper:#f1f2ec;
  --ink:#1d1d1d;
  --stage:#e4e4e4;
  --heading:"Signika",sans-serif;
  --body:"Questrial",sans-serif;
}
*{box-sizing:border-box;margin:0;padding:0}
html,body{width:1200px;height:800px;overflow:hidden;background:var(--stage)}
.brochure{position:absolute;left:60px;top:40px;width:1080px;height:720px;display:flex;box-shadow:0 6px 22px rgba(0,0,0,.18)}
.panel{position:relative;width:360px;height:720px;overflow:hidden}
.panel svg.shape{position:absolute;left:0;top:0}

/* left panel */
.panel--about{background:var(--sky)}
.team-photo{position:absolute;left:0;top:0;width:360px;height:320px;background:linear-gradient(160deg,#8d9aa4 0%,#5d6a72 45%,#3f4a40 100%)}
.info-card{position:absolute;left:24px;width:314px;background:var(--charcoal);color:#fff;border:2px solid #fff;box-shadow:0 3px 8px rgba(0,0,0,.35);padding:32px 18px 12px}
.info-card__title{position:absolute;left:-12px;top:-16px;background:var(--green);color:#fff;font:600 18px/1 var(--heading);padding:9px 14px;white-space:nowrap;box-shadow:0 2px 4px rgba(0,0,0,.3)}
.info-card p{font:13px/1.4 var(--body)}
.info-card--about{top:344px}
.info-card--mission{top:540px}

/* middle panel */
.panel--why{background:var(--paper)}
.why__title{position:absolute;top:62px;left:0;width:100%;text-align:center;color:var(--sky);font:600 25px/1.15 var(--heading)}
.why__text{position:absolute;top:136px;left:36px;width:288px;text-align:center;font:13px/1.45 var(--body);color:var(--ink)}
.why__text strong{color:var(--blue);font-weight:700}
.bin-blue{position:absolute;left:100px;top:300px;width:160px;height:170px;background:linear-gradient(150deg,#3a8ee6,#0f55b8);border-radius:10px 10px 26px 26px}
.contact-card{position:absolute;left:26px;top:524px;width:308px;height:160px;background:var(--charcoal);border:2px solid #fff;box-shadow:0 3px 8px rgba(0,0,0,.3);color:#fff;text-align:center;padding:40px 10px 0}
.contact-card__title{position:absolute;left:-10px;right:-10px;top:-18px;background:var(--green);font:600 22px/1 var(--heading);padding:10px 0;text-align:center}
.contact-card__name{font:700 15px/1.4 var(--body)}
.contact-card p{font:14px/1.4 var(--body)}
.contact-card .contact-card__phone{font:700 16px/1.4 var(--body)}

/* right panel */
.panel--cover{background:var(--paper)}
.brand{position:absolute;top:40px;left:40px;display:flex;align-items:center;gap:10px}
.brand__dot{width:26px;height:26px;border-radius:50%;background:var(--orange)}
.brand__name{font:600 21px/1 var(--heading);color:var(--blue)}
.cover__headline{position:absolute;top:118px;right:34px;text-align:right;font:700 29px/1.15 var(--heading);color:var(--blue)}
.cover__headline .accent{color:var(--green-deep)}
.bin-yellow{position:absolute;left:110px;top:220px;width:170px;height:230px;background:linear-gradient(160deg,#ffe34a,#f2c200);border-radius:12px 12px 20px 20px}
.cover__url{position:absolute;left:0;bottom:0;width:100%;height:44px;background:var(--orange);color:#fff;font:15px/44px var(--body);text-align:right;padding-right:24px}
</style>
</head>
<body>
<main class="brochure">

  <section class="panel panel--about">
    <div class="team-photo" role="img" aria-label="Photo of the owner standing beside an apartment dumpster, carrying a trash bag, under a cloudy sky"></div>
    <svg class="shape" width="360" height="720" viewBox="0 0 360 720" aria-hidden="true">
      <path d="M0 320 L0 292 Q200 320 300 165 Q340 88 360 78 L360 320 Z" fill="var(--sky)"/>
      <path d="M0 292 Q200 320 300 165 Q330 112 360 92 Q330 156 310 195 Q220 336 0 310 Z" fill="var(--green)"/>
      <path d="M150 90 Q290 60 360 70 L360 85 Q300 76 150 90 Z" fill="var(--green)"/>
    </svg>
    <article class="info-card info-card--about">
      <h2 class="info-card__title">About Curbside Bin Butler</h2>
      <p>Curbside Bin Butler is a Houston-based valet trash service created by Marcus Hale, Bayou City College alumni and professional mixed martial artist. Young life experiences at Trailhead Youth made him want to live a life with less impact on the environment.</p>
    </article>
    <article class="info-card info-card--mission">
      <h2 class="info-card__title">Recycling is what it is all about.</h2>
      <p>At Curbside Bin Butler, recycling is a way of life. We collect sorted recyclables from apartment doorsteps along with the trash, so tenants can reduce, reuse and recycle with no extra trips.</p>
    </article>
  </section>

  <section class="panel panel--why">
    <h2 class="why__title">Why Choose<br>Curbside Bin Butler?</h2>
    <p class="why__text"><strong>Tenants:</strong> set your bag outside your door on pickup nights and we carry it to the dumpster. No late walks across the lot. <strong>Management:</strong> cleaner breezeways, tidy dumpster areas, fewer complaints and an amenity that keeps residents renewing.</p>
    <div class="bin-blue" role="img" aria-label="Blue recycling bin with open lid"></div>
    <article class="contact-card">
      <h2 class="contact-card__title">Let's Talk.</h2>
      <p class="contact-card__name">Curbside Bin Butler</p>
      <p>2840 Larkspur Ave #210<br>Fairview, TX 77000</p>
      <p class="contact-card__phone">T: (555) 014-2290</p>
      <p>hello@curbsidebinbutler.example</p>
    </article>
  </section>

  <section class="panel panel--cover">
    <svg class="shape" width="360" height="720" viewBox="0 0 360 720" aria-hidden="true">
      <path d="M330 70 Q140 80 80 170 Q40 240 90 300 Q60 230 110 175 Q170 110 330 70 Z" fill="var(--orange)"/>
      <path d="M0 720 L0 560 Q180 470 360 420 L360 720 Z" fill="var(--blue)"/>
      <path d="M0 560 Q140 480 260 500 Q300 470 280 400 Q330 440 330 470 Q200 470 0 580 Z" fill="var(--green-deep)"/>
    </svg>
    <div class="brand">
      <span class="brand__dot"></span>
      <span class="brand__name">Curbside Bin Butler</span>
    </div>
    <h1 class="cover__headline">Recycle...<br>it's <span class="accent">easy!</span></h1>
    <div class="bin-yellow" role="img" aria-label="Yellow wheeled recycling bin wrapped in green recycling arrows"></div>
    <p class="cover__url">www.curbsidebinbutler.example</p>
  </section>

</main>
</body>
</html>
```